updated documents

Hi i have included a new picture for the about us section, i have also included the updated word document, all changes have been highlighted.

Thanks,

Leon

```html
<!DOCTYPE html>
<html lang="en">
<head>
<meta charset="utf-8">
<title>Keystone Building Care – Brochure Cover</title>
<link rel="stylesheet" href="https://fonts.googleapis.com/css2?family=Cinzel:wght@400&family=Open+Sans:wght@600&display=swap">
<style>
  :root {
    --backdrop: #dcdcdc;
    --photo-highlight: #d9d4d2;
    --photo-light: #a39d9b;
    --photo-mid: #6b6564;
    --photo-dark: #2a2727;
    --photo-deep: #161414;
    --panel: rgba(200, 200, 200, 0.84);
    --brand-grey: #4f4f4f;
    --accent: #a6c72a;
    --band: #0b0b0b;
    --tagline: #ffffff;
  }
  html, body {
    margin: 0;
    padding: 0;
    width: 1184px;
    height: 1200px;
    overflow: hidden;
    background: var(--backdrop);
  }
  .cover {
    position: absolute;
    left: 192px;
    top: 30px;
    width: 800px;
    height: 1140px;
    overflow: hidden;
    background: var(--photo-mid);
    box-shadow: 0 10px 30px rgba(0, 0, 0, 0.25);
  }
  .cover__photo {
    position: absolute;
    inset: 0 0 92px 0;
    background:
      radial-gradient(ellipse 22% 14% at 58% 12%, var(--photo-highlight) 0%, transparent 100%),
      radial-gradient(ellipse 18% 12% at 22% 52%, var(--photo-highlight) 0%, transparent 100%),
      radial-gradient(ellipse 14% 20% at 36% 70%, var(--photo-light) 0%, transparent 100%),
      radial-gradient(ellipse 26% 30% at 66% 36%, var(--photo-deep) 0%, transparent 100%),
      radial-gradient(ellipse 20% 26% at 38% 30%, var(--photo-dark) 0%, transparent 100%),
      radial-gradient(ellipse 30% 24% at 12% 20%, var(--photo-light) 0%, transparent 100%),
      radial-gradient(ellipse 24% 30% at 90% 70%, var(--photo-light) 0%, transparent 100%),
      radial-gradient(ellipse 20% 18% at 20% 88%, var(--photo-dark) 0%, transparent 100%),
      linear-gradient(165deg, var(--photo-mid) 0%, var(--photo-dark) 45%, var(--photo-mid) 75%, var(--photo-light) 100%);
  }
  .cover__brand-panel {
    position: absolute;
    left: 232px;
    top: 520px;
    width: 470px;
    height: 370px;
    background: var(--panel);
    display: flex;
    align-items: center;
    justify-content: center;
    gap: 12px;
  }
  .brand-mark {
    width: 16px;
    height: 16px;
    background: var(--accent);
  }
  .brand-name {
    font-family: "Cinzel", serif;
    font-weight: 400;
    font-size: 26px;
    letter-spacing: 0.5px;
    color: var(--brand-grey);
  }
  .cover__band {
    position: absolute;
    left: 0;
    right: 0;
    bottom: 0;
    height: 92px;
    background: var(--band);
    display: flex;
    align-items: center;
    justify-content: center;
  }
  .tagline {
    font-family: "Open Sans", sans-serif;
    font-weight: 600;
    font-size: 22px;
    letter-spacing: 0.6px;
    color: var(--tagline);
    margin: 0;
  }
</style>
</head>
<body>
  <main class="cover">
    <div class="cover__photo" role="img" aria-label="Black and white aerial view looking down on dense city high-rise buildings, rooftops and streets"></div>
    <div class="cover__brand-panel">
      <span class="brand-mark"></span>
      <span class="brand-name">Keystone Building Care</span>
    </div>
    <footer class="cover__band">
      <p class="tagline">Your Best Partner in Building Maintenance</p>
    </footer>
  </main>
</body>
</html>
```